Business Cards for Harbourline Coatings Pty Ltd

Hi every one i need a design for my buisness cards. I Want my logo in it and the name of the company needs to stand out Harbourline Coatings Pty Ltd. I want the background of the buisness cards black and i want the font to stand out in either a white or a silver stylish text. I want the design to be simple but original not to in your face if you know what i mean. I want on the back of the buisness cards to have the services that my buisness offers.
• Interior/Exterior
• Residential/Commercial
• Special effects/Texture Coatings
• Water Damage Repair
• Fully qualified
• Pensioner Discount
• 10 Year guarantee
• Fully Insured
• Obligation free quotes
full internal repaints include a proffesionla cleaning service
I want the services on the back to be layed out in an originall way not just dot points. If possible could my logo take up the whole back ground of the back but the text with the services be kind of like transparent so u cvan still see the logo i dont know if its possible it woiuld just look cool if possible. When i pick a design ill give my contact details to the designer to add to the design at the end. Any questions please just ask! Ill upload my logo.
Conatcs will include office phone: Mobile: E-mail - dale@harbourlinecoatings.com.au, Ill also have a Postal address which is a PO Box and my website is www.harbourlinecoatings.com.au

```html
<!DOCTYPE html>
<html lang="en">
<head>
<meta charset="utf-8">
<title>Harbourline Coatings Pty Ltd — Business Cards</title>
<link href="https://fonts.googleapis.com/css2?family=Questrial&family=Open+Sans:wght@400&display=swap" rel="stylesheet">
<style>
  :root {
    --page-bg: #5a544c;
    --card-black: #000000;
    --card-dark: #2a2a2a;
    --silver-light: #e6e6e6;
    --silver: #bdbdbd;
    --text-white: #ffffff;
  }
  html, body {
    margin: 0;
    padding: 0;
    width: 849px;
    height: 1200px;
    overflow: hidden;
    background: var(--page-bg);
  }
  .canvas {
    position: relative;
    width: 849px;
    height: 1200px;
  }
  .card {
    position: absolute;
    width: 359px;
    height: 205px;
    box-sizing: border-box;
  }
  .card-front {
    left: 100px;
    top: 300px;
    background: var(--card-black);
    text-align: center;
    z-index: 1;
  }
  .brand-square {
    position: absolute;
    left: 128px;
    top: 11px;
    width: 102px;
    height: 106px;
    background: var(--silver);
  }
  .company-name {
    position: absolute;
    left: 0;
    right: 0;
    top: 130px;
    margin: 0;
    font-family: "Questrial", sans-serif;
    font-weight: 400;
    font-size: 23px;
    letter-spacing: 0.5px;
    color: var(--silver-light);
  }
  .company-suffix {
    position: absolute;
    left: 0;
    right: 0;
    top: 166px;
    margin: 0;
    font-family: "Questrial", sans-serif;
    font-size: 16px;
    color: var(--silver-light);
  }
  .card-back {
    left: 356px;
    top: 502px;
    background: radial-gradient(ellipse at 50% 45%, var(--card-dark) 0%, #141414 55%, var(--card-black) 100%);
    border: 5px solid var(--card-black);
    text-align: center;
    color: var(--text-white);
    font-family: "Open Sans", sans-serif;
    z-index: 2;
  }
  .services {
    list-style: none;
    margin: 4px 0 0;
    padding: 0;
    font-size: 7.6px;
    line-height: 10.8px;
    color: #e8e8e8;
  }
  .contacts {
    margin: 5px 0 0;
    font-size: 13px;
    line-height: 17px;
    letter-spacing: 0.2px;
  }
  .contacts p { margin: 0; }
</style>
</head>
<body>
<main class="canvas">
  <section class="card card-front">
    <div class="brand-square"></div>
    <h1 class="company-name">HARBOURLINE COATINGS</h1>
    <p class="company-suffix">PTY LTD</p>
  </section>

  <section class="card card-back">
    <ul class="services">
      <li>Interior/Exterior</li>
      <li>Residential/Commercial</li>
      <li>Special effects/Texture Coatings</li>
      <li>Water Damage Repair</li>
      <li>Fully qualified</li>
      <li>Pensioner Discount</li>
      <li>10 Year guarantee</li>
      <li>Fully Insured</li>
      <li>Obligation free quotes</li>
      <li>Full internal repaints include a free proffesional cleaning service</li>
    </ul>
    <div class="contacts">
      <p>Office:(02) 6100 4821</p>
      <p>Mobile: 0400 318 945</p>
      <p>www.harbourlinecoatings.com.au</p>
      <p>E-mail: dale@harbourlinecoatings.com.au</p>
    </div>
  </section>
</main>
</body>
</html>
```